Tech business card design

We need an amazing business card design for our new business 'Brakka' a marketing tech startup based in Sydney, Australia. We provide an online marketplace for businesses to search and buy advertising media, connect with service providers and learn more about marketing. We wish to communicate 'cool tech', reliability and professionalism and design based around our logo.

Target Market(s)

Business Owners

Contact Information for Business Card

Name
Position
Email Address
Website
Phone Number

Font styles to use
Other font styles liked:
• Avenir & Avenir Next

Colors

Designer to choose colors to be used in the design.

```html
<!DOCTYPE html>
<html lang="en">
<head>
<meta charset="utf-8">
<title>Brakka — Business Card</title>
<link rel="stylesheet" href="https://fonts.googleapis.com/css2?family=Mulish:wght@300;400;800&display=swap">
<style>
  :root {
    --navy: #14143f;
    --white: #ffffff;
    --backdrop: #e6e6e6;
    --ink: #14143f;
    --muted: #3a3a5c;
  }
  * { box-sizing: border-box; margin: 0; padding: 0; }
  html, body {
    width: 1200px;
    height: 900px;
    overflow: hidden;
    background: var(--backdrop);
    font-family: "Mulish", "Avenir Next", Avenir, sans-serif;
  }
  .stage {
    width: 1200px;
    height: 900px;
    display: flex;
    flex-direction: column;
    align-items: center;
    justify-content: center;
    gap: 40px;
  }
  .card {
    position: relative;
    width: 600px;
    height: 367px;
    box-shadow: 0 6px 18px rgba(0,0,0,0.12);
    overflow: hidden;
  }
  /* Front */
  .card--front {
    background: var(--navy);
    color: var(--white);
    display: flex;
    flex-direction: column;
    align-items: center;
    justify-content: center;
  }
  .brand-name {
    font-weight: 800;
    letter-spacing: -1px;
    line-height: 1;
  }
  .card--front .brand-name {
    font-size: 96px;
    color: var(--white);
    margin-top: 10px;
  }
  .front-url {
    margin-top: 52px;
    font-size: 20px;
    font-weight: 300;
    letter-spacing: 0.5px;
  }
  /* Back */
  .card--back {
    background: var(--white);
    color: var(--ink);
  }
  .accent-bar {
    position: absolute;
    left: 0;
    top: 118px;
    width: 7px;
    height: 42px;
    background: var(--navy);
  }
  .identity {
    position: absolute;
    left: 38px;
    top: 112px;
  }
  .person-name {
    font-size: 22px;
    font-weight: 800;
    line-height: 1.1;
  }
  .person-role {
    font-size: 21px;
    font-weight: 300;
    color: var(--muted);
    line-height: 1.2;
  }
  .divider {
    position: absolute;
    left: 38px;
    top: 210px;
    width: 24px;
    height: 2px;
    background: var(--navy);
  }
  .contact-list {
    position: absolute;
    left: 38px;
    top: 254px;
    list-style: none;
  }
  .contact-item {
    display: flex;
    align-items: center;
    gap: 12px;
    font-size: 19px;
    font-weight: 400;
    line-height: 1.25;
    color: var(--ink);
  }
  .contact-icon {
    width: 15px;
    height: 15px;
    flex: none;
  }
  .card--back .brand-name {
    position: absolute;
    right: 22px;
    top: 50%;
    font-size: 84px;
    color: var(--navy);
    writing-mode: vertical-rl;
    transform: translateY(-50%);
  }
</style>
</head>
<body>
  <main class="stage">
    <section class="card card--front" aria-label="Card front">
      <div class="brand-name">brakka</div>
      <p class="front-url">www.brakkamedia.com.au</p>
    </section>

    <section class="card card--back" aria-label="Card back">
      <span class="accent-bar"></span>
      <div class="identity">
        <p class="person-name">Liam Carver</p>
        <p class="person-role">Founder, Director</p>
      </div>
      <span class="divider"></span>
      <ul class="contact-list">
        <li class="contact-item">
          <svg class="contact-icon" viewBox="0 0 24 24" aria-hidden="true"><path fill="#14143f" d="M6.6 10.8a15 15 0 0 0 6.6 6.6l2.2-2.2a1 1 0 0 1 1-.25 11.4 11.4 0 0 0 3.6.57 1 1 0 0 1 1 1V20a1 1 0 0 1-1 1A17 17 0 0 1 3 4a1 1 0 0 1 1-1h3.5a1 1 0 0 1 1 1c0 1.25.2 2.46.57 3.6a1 1 0 0 1-.25 1z"/></svg>
          <span>+61 (0)400 555 218</span>
        </li>
        <li class="contact-item">
          <svg class="contact-icon" viewBox="0 0 24 24" aria-hidden="true"><path fill="#14143f" d="M2 5h20v14H2z"/><path fill="none" stroke="#fff" stroke-width="1.8" d="M2.5 5.5 12 13l9.5-7.5"/></svg>
          <span>liam@brakkamedia.com.au</span>
        </li>
        <li class="contact-item">
          <svg class="contact-icon" viewBox="0 0 24 24" aria-hidden="true"><circle cx="12" cy="12" r="10" fill="#14143f"/><g fill="none" stroke="#fff" stroke-width="1.3"><ellipse cx="12" cy="12" rx="4" ry="10"/><path d="M2 12h20M4 7h16M4 17h16"/></g></svg>
          <span>www.brakkamedia.com.au</span>
        </li>
      </ul>
      <div class="brand-name">brakka</div>
    </section>
  </main>
</body>
</html>
```